Book cover design for Kiwis handbook to cruising Canada

I need an awesome book cover designed for my upcoming book “Kiwis Handbook to Cruising Canada”, featuring the ledgendary Brockvale motorcycle rally.I would like to use the photo supplied.I require an image that can be used for bookcover hardcopy, front, back and spine. I also need design for Ebooks. The book is currently at the editors and I am estimating a page count of 270pages.The book is aimed as a guide for the many Australians that travel to America each year for Brockvale (biggest motorcycle rally in the world). Book size 9x6”

Target Market(s)

Travel, Motorcyclists, Corwin Talbert,

Font styles to use
Serif
Sans Serif

Colors

Designer to choose colors to be used in the design.

Requirements
Must have
• Title: Kiwis Handbook to Cruising Canada ,
• Subtitle: featuring the Ledgendary BROCKVALE motorcycle rally.
• Author name: Greta Pasko
• Front cober, spine, rear cover(with room to add a blurb about the book.
Nice to have
• Would like to use photo with orange bike at Quarrel basin. I have many more images if required. Would like to see a bald eagle and possibly American flag colours through the lettering for America.
• “Aussies guide to”, in smaller lettering (highlight the words “Roadtripping America” a bit more).

```html
<!DOCTYPE html>
<html lang="en">
<head>
<meta charset="utf-8">
<title>Kiwis Handbook to Cruising Canada – Greta Pasko</title>
<link rel="stylesheet" href="https://fonts.googleapis.com/css2?family=Cinzel:wght@400;500;600&family=Anton&display=swap">
<style>
  :root {
    --stage: #1b1b1c;
    --sky-deep: #14577f;
    --sky-mid: #3d86ae;
    --sky-haze: #8fb3bf;
    --glow: #e9c27a;
    --sunset: #f3a43a;
    --mesa: #b0522a;
    --desert: #8a6a40;
    --scrub: #6f6a45;
    --road: #3a3f4c;
    --road-dark: #1f2129;
    --bike: #c8471f;
    --ink-light: #ffffff;
    --title-red: #c8242c;
    --title-blue: #1f3f8a;
    --shadow: rgba(0, 0, 0, 0.6);
  }
  * { margin: 0; padding: 0; box-sizing: border-box; }
  html, body {
    width: 1200px;
    height: 905px;
    overflow: hidden;
    background: var(--stage);
  }
  .canvas {
    position: relative;
    width: 1200px;
    height: 905px;
    display: flex;
    justify-content: center;
  }
  .front-cover {
    position: relative;
    width: 603px;
    height: 905px;
    overflow: hidden;
  }
  .photo-sky {
    position: absolute;
    left: 0; right: 0; top: 0;
    height: 580px;
    background: linear-gradient(180deg,
      var(--sky-deep) 0%,
      var(--sky-mid) 35%,
      var(--sky-haze) 62%,
      var(--glow) 85%,
      var(--sunset) 100%);
  }
  .photo-ground {
    position: absolute;
    left: 0; right: 0; top: 580px; bottom: 0;
    background:
      radial-gradient(ellipse 45% 55% at 72% 78%, var(--bike) 0%, rgba(200, 71, 31, 0.55) 40%, rgba(200, 71, 31, 0) 75%),
      linear-gradient(180deg,
        var(--mesa) 0%,
        var(--desert) 14%,
        var(--scrub) 30%,
        var(--road) 52%,
        var(--road-dark) 100%);
  }
  .author-name {
    position: absolute;
    top: 58px;
    left: 0;
    right: 0;
    text-align: center;
    font-family: "Cinzel", serif;
    font-weight: 500;
    font-size: 54px;
    letter-spacing: -0.5px;
    color: var(--ink-light);
    text-shadow: 2px 3px 6px var(--shadow);
  }
  .title-block {
    position: absolute;
    top: 232px;
    left: 76px;
    width: 470px;
    transform: rotate(-10deg);
    transform-origin: left top;
  }
  .title-lead {
    display: block;
    font-family: "Cinzel", serif;
    font-weight: 500;
    font-size: 38px;
    line-height: 1;
    color: var(--ink-light);
    text-shadow: 1px 2px 4px var(--shadow);
  }
  .title-bridge {
    display: block;
    font-family: "Cinzel", serif;
    font-size: 19px;
    letter-spacing: 6px;
    color: rgba(255, 255, 255, 0.85);
    margin: 2px 0 0 4px;
  }
  .title-main {
    display: block;
    font-family: "Anton", sans-serif;
    font-size: 150px;
    line-height: 0.95;
    letter-spacing: 2px;
    color: var(--title-red);
    -webkit-text-stroke: 2px var(--ink-light);
    text-shadow: 4px 5px 0 var(--title-blue), 6px 9px 10px var(--shadow);
  }
  .subtitle {
    position: absolute;
    top: 796px;
    left: 130px;
    width: 330px;
    text-align: center;
    white-space: nowrap;
    font-family: "Cinzel", serif;
    font-size: 17px;
    line-height: 1.3;
    color: var(--ink-light);
    transform: rotate(5deg);
    text-shadow: 1px 1px 4px var(--shadow), 0 0 2px var(--shadow);
  }
  .subtitle .rally-name { font-size: 19px; }
</style>
</head>
<body>
  <main class="canvas">
    <section class="front-cover">
      <div class="photo-sky" role="img" aria-label="Photograph of a blue sunset sky with wispy clouds and a bald eagle soaring, wings spread"></div>
      <div class="photo-ground" role="img" aria-label="Photograph of red mesas at Quarrel basin on the horizon, a straight desert road, and an orange touring motorcycle with a flag and saddlebags in the foreground"></div>
      <h2 class="author-name">Greta Pasko</h2>
      <h1 class="title-block">
        <span class="title-lead">Kiwis Handbook</span>
        <span class="title-bridge">to cruising</span>
        <span class="title-main">CANADA</span>
      </h1>
      <p class="subtitle">Featuring the Ledgendary<br><span class="rally-name">BROCKVALE</span> motorcycle rally</p>
    </section>
  </main>
</body>
</html>
```